Pest control

Pest solutions to all residential and commercial sites, the technicians name will be displayed on the back of the card, and a description of his duties: Pest Technician, Termite Inspector,
Termite protection of properties.
The colours will be all white with VARNO and the 1300 482 157 be a blue.
The file with the phone icon is from my web site.
Residential
VARNO PEST SOLUTIONS, 1300 482 157
varno-example.com.au
info@varno-example.com.au

```html
<!DOCTYPE html>
<html lang="en">
<head>
<meta charset="utf-8">
<title>Varno Pest Solutions – Business Cards</title>
<link rel="stylesheet" href="https://fonts.googleapis.com/css2?family=Arimo:wght@400;700&display=swap">
<style>
  :root {
    --brand-blue: #1e95c9;
    --card-black: #0e0e0e;
    --card-white: #ffffff;
    --text-dark: #111111;
    --phone-green: #3fae3a;
    --stage: #e9e9ea;
  }
  * { box-sizing: border-box; margin: 0; padding: 0; }
  html, body {
    width: 1200px; height: 1000px; overflow: hidden;
    background: var(--stage);
    font-family: "Arimo", Arial, sans-serif;
  }
  .card {
    position: absolute; left: 200px;
    width: 800px; height: 457px;
    overflow: hidden;
    box-shadow: 0 6px 18px rgba(0,0,0,.18);
  }

  /* ---------- Front card ---------- */
  .card--front { top: 28px; background: var(--card-white); }
  .front__panel {
    position: absolute; left: 340px; top: 128px; right: 0; bottom: 0;
    background: var(--card-black);
  }
  .brand { position: absolute; left: 44px; top: 150px; width: 285px; }
  .brand__name {
    font-weight: 700; font-size: 64px; line-height: .9;
    color: var(--brand-blue); letter-spacing: 1px;
  }
  .brand__tagline {
    font-size: 20px; color: var(--text-dark);
    letter-spacing: -.3px; margin-top: 4px;
  }
  .brand__phone {
    display: flex; align-items: center; gap: 8px; margin-top: 10px;
    white-space: nowrap;
  }
  .phone-icon {
    flex: none;
    width: 32px; height: 32px; border-radius: 4px;
    background: var(--phone-green);
    display: flex; align-items: center; justify-content: center;
  }
  .brand__number {
    font-weight: 700; font-size: 32px; color: var(--brand-blue);
  }
  .duties { position: absolute; left: 270px; top: 318px; right: 0; list-style: none; }
  .duty {
    height: 34px; margin-bottom: 9px;
    background: var(--brand-blue);
    clip-path: polygon(14px 0, 100% 0, 100% 100%, 0 100%);
    display: flex; align-items: center; gap: 10px;
    padding-left: 30px;
    color: var(--card-white); font-size: 17px;
  }

  /* ---------- Back card ---------- */
  .card--back { top: 515px; background: var(--card-black); }
  .back__contact {
    position: absolute; left: 70px; top: 42px;
    color: var(--brand-blue); font-size: 17px; line-height: 1.25;
  }
  .back__contact span { display: block; }
  .back__contact span + span { padding-left: 28px; }
  .back__rule {
    position: absolute; left: 0; right: 0; top: 94px;
    height: 1px; background: var(--brand-blue);
  }
  .back__band {
    position: absolute; left: 0; right: 0; top: 272px; height: 38px;
    background: var(--brand-blue);
  }
  .back__name {
    position: absolute; right: 70px; top: 198px;
    font-weight: 700; font-size: 72px; line-height: 1;
    color: var(--card-white); letter-spacing: 2px;
  }
  .back__tagline {
    position: absolute; right: 70px; top: 278px;
    font-size: 24px; color: var(--text-dark); letter-spacing: .5px;
  }
  .back__number {
    position: absolute; right: 110px; top: 326px;
    font-weight: 700; font-size: 32px; color: var(--card-white);
    letter-spacing: 1px;
  }
</style>
</head>
<body>

<section class="card card--front" aria-label="Card front">
  <div class="front__panel"></div>
  <div class="brand">
    <div class="brand__name">VARNO</div>
    <div class="brand__tagline">PEST SOLUTIONS</div>
    <div class="brand__phone">
      <span class="phone-icon">
        <svg width="20" height="20" viewBox="0 0 24 24" aria-hidden="true">
          <path fill="#fff" d="M6.6 10.8a15.2 15.2 0 0 0 6.6 6.6l2.2-2.2a1 1 0 0 1 1-.25 11.4 11.4 0 0 0 3.6.57 1 1 0 0 1 1 1V20a1 1 0 0 1-1 1A17 17 0 0 1 3 4a1 1 0 0 1 1-1h3.5a1 1 0 0 1 1 1c0 1.25.2 2.45.57 3.57a1 1 0 0 1-.25 1z"/>
        </svg>
      </span>
      <span class="brand__number">1300 482 157</span>
    </div>
  </div>
  <ul class="duties">
    <li class="duty"><svg width="16" height="14" viewBox="0 0 16 14" aria-hidden="true"><path d="M1 7.5l4.5 4.5L15 2" fill="none" stroke="#fff" stroke-width="3"/></svg>Pest Technician</li>
    <li class="duty"><svg width="16" height="14" viewBox="0 0 16 14" aria-hidden="true"><path d="M1 7.5l4.5 4.5L15 2" fill="none" stroke="#fff" stroke-width="3"/></svg>Termite Inspector</li>
    <li class="duty"><svg width="16" height="14" viewBox="0 0 16 14" aria-hidden="true"><path d="M1 7.5l4.5 4.5L15 2" fill="none" stroke="#fff" stroke-width="3"/></svg>Termite protection of properties.</li>
  </ul>
</section>

<section class="card card--back" aria-label="Card back">
  <div class="back__contact">
    <span>www.varno-example.com.au</span>
    <span>info@varno-example.com.au</span>
  </div>
  <div class="back__rule"></div>
  <div class="back__band"></div>
  <div class="back__name">VARNO</div>
  <div class="back__tagline">PEST SOLUTION</div>
  <div class="back__number">1300 482 157</div>
</section>

</body>
</html>
```